**SUPER EASY AND QUICK - 2 LABELS FOR MASON JAR (JAR AND LID LABEL)

This is going to be a super easy project for someone who can think of a quick great idea!!!! We want to pick a winner really quick, so give us all you got.

I included a sample picture to make it real eazy!!!!

We are filling 8 oz mason jars with CARAMEL POPCORN and dropping them as thank you treats!!!! We need a 2 x 4 label for the base of the jar, and also a 2.5 in circle for lid!!!

We want to have a design with a caramel popcorn border, or caramel popcorn pieces on the labels.

We need to incorporate our logo on the labels also.

We also need the words "We Were Just popping By To Say Thanks!!!"

The font should be something bubbly and fun, like popcorn!!! Not just a plain boring font.

Our company colors are silver and chocolate brown, so we need to incorporate the labels to have colors that match that.
I HAVE UPLOADED A LOT OF STUFF TO MAKE IT EAZY!!!

AGAIN.....SUPER EASY, QUICK AND FUN PROJECT!!!! WE WANT TO PICK A WINNER FAST!!!!

Requirements
Must have
• Popcorn images on the label, our logo and also try to use our colors or colors that match our company colors (silver and chocolate brown). I would like to use "caramel popcorn images", as they look better than regular popcorn images.
• Words "We Were Just Popping By To Say THANKS!!!!"
• Fun Looking Fonts that stand out!!!!
• WE WANT COLORFUL!!!
Should not have
• NO PLAIN FONTS

```html
<!DOCTYPE html>
<html lang="en">
<head>
<meta charset="utf-8">
<title>Popping By – Jar Labels</title>
<link rel="stylesheet" href="https://fonts.googleapis.com/css2?family=Sniglet:wght@400;800&family=Quicksand:wght@500;600&display=swap">
<style>
  :root {
    --page: #f2f2f2;
    --page-edge: #e2e2e2;
    --silver: #a4a4a4;
    --silver-rim: #c9c9c9;
    --silver-rim-dark: #9a9a9a;
    --chocolate: #6a3a10;
    --caramel-dark: #8a4e12;
    --caramel: #c9862e;
    --caramel-light: #e7b66a;
    --cream: #f5ecdc;
    --white: #ffffff;
  }
  * { margin: 0; padding: 0; box-sizing: border-box; }
  html, body { width: 1200px; height: 1200px; overflow: hidden; }
  body {
    background: radial-gradient(circle at 50% 40%, var(--white) 0%, var(--page) 60%, var(--page-edge) 100%);
    position: relative;
    font-family: "Sniglet", "Comic Sans MS", cursive;
  }

  .headline {
    font-weight: 800;
    line-height: 1;
    white-space: nowrap;
    text-shadow:
      -2px -2px 0 var(--white), 2px -2px 0 var(--white),
      -2px 2px 0 var(--white), 2px 2px 0 var(--white),
      3px 4px 4px rgba(0,0,0,0.35);
  }
  .headline .silver { color: var(--silver); }
  .headline .brown { color: var(--chocolate); }

  .brand {
    display: flex; align-items: center; gap: 8px;
    position: absolute;
  }
  .brand-dot {
    width: 30px; height: 30px; border-radius: 50%;
    background: var(--chocolate); flex: none;
  }
  .brand-text { display: flex; flex-direction: column; line-height: 1; }
  .brand-name {
    font-family: "Sniglet", "Comic Sans MS", cursive;
    font-weight: 400; font-size: 26px; color: var(--chocolate);
  }
  .brand-tag {
    font-family: "Quicksand", Arial, sans-serif;
    font-weight: 600; font-size: 10px; color: var(--chocolate);
    margin-top: 3px; letter-spacing: 0.2px;
  }

  /* Lid label */
  .lid-label {
    position: absolute; left: 330px; top: 18px;
    width: 564px; height: 564px; border-radius: 50%;
    background: linear-gradient(145deg, var(--silver-rim) 0%, #e4e4e4 45%, var(--silver-rim-dark) 100%);
    box-shadow: 0 6px 14px rgba(0,0,0,0.35);
  }
  .lid-popcorn {
    position: absolute; left: 16px; top: 16px;
    width: 532px; height: 532px; border-radius: 50%;
    background:
      radial-gradient(circle at 35% 30%, var(--caramel-light) 0%, transparent 40%),
      radial-gradient(circle at 70% 70%, var(--caramel-dark) 0%, transparent 45%),
      radial-gradient(circle at 50% 50%, var(--caramel) 0%, var(--caramel-dark) 100%);
  }
  .lid-label .brand { left: 206px; top: 76px; }
  .lid-headline {
    position: absolute; left: 0; width: 564px; text-align: center;
  }
  .lid-line-1 { top: 172px; font-size: 60px; }
  .lid-line-2 { top: 248px; font-size: 60px; }
  .lid-line-3 { top: 346px; font-size: 60px; left: -20px; }
  .lid-line-4 { top: 424px; font-size: 62px; left: -20px; }

  /* Jar label */
  .jar-label {
    position: absolute; left: 56px; top: 628px;
    width: 1092px; height: 545px;
    background: var(--white);
    border: 1px solid #888;
    box-shadow: 0 6px 12px rgba(0,0,0,0.35);
  }
  .jar-popcorn {
    position: absolute; left: 4px; top: 20px; right: 4px; bottom: 12px;
    background:
      linear-gradient(180deg,
        var(--caramel) 0%, var(--caramel-light) 14%,
        var(--cream) 30%, #faf4ea 50%, var(--cream) 70%,
        var(--caramel-light) 86%, var(--caramel) 100%);
  }
  .jar-headline { position: absolute; }
  .jar-line-1 { left: 124px; top: 200px; font-size: 60px; }
  .jar-line-2 { left: 172px; top: 278px; font-size: 64px; }
  .jar-label .brand { left: 852px; top: 330px; }
</style>
</head>
<body>

  <section class="lid-label" aria-label="Lid label">
    <div class="lid-popcorn" role="img" aria-label="Close-up photo of caramel popcorn filling the circle"></div>
    <div class="brand">
      <span class="brand-dot"></span>
      <span class="brand-text">
        <span class="brand-name">Harbor Path</span>
        <span class="brand-tag">a pro active addiction center</span>
      </span>
    </div>
    <p class="headline lid-headline lid-line-1"><span class="silver">We Were Just</span></p>
    <p class="headline lid-headline lid-line-2"><span class="silver">popping By</span></p>
    <p class="headline lid-headline lid-line-3"><span class="brown">To Say</span></p>
    <p class="headline lid-headline lid-line-4"><span class="brown">Thanks!!!</span></p>
  </section>

  <section class="jar-label" aria-label="Jar label">
    <div class="jar-popcorn" role="img" aria-label="Caramel popcorn photo along the top and bottom, faded to cream in the middle"></div>
    <p class="headline jar-headline jar-line-1"><span class="silver">We Were Just popping By</span></p>
    <p class="headline jar-headline jar-line-2"><span class="brown">To Say Thanks!!!</span></p>
    <div class="brand">
      <span class="brand-dot"></span>
      <span class="brand-text">
        <span class="brand-name">Harbor Path</span>
        <span class="brand-tag">a pro active addiction center</span>
      </span>
    </div>
  </section>

</body>
</html>
```